Recruitment talent email to send employers

We are a recruitment company specialising in STEM talent. We're after an eye catching email design to send our clients (ie employers) information about our top cadidates.

Target Market(s)

Employers

Requirements
Must have
• Must be clean/fresh looking, professional and concise

```html
<!DOCTYPE html>
<html lang="en">
<head>
<meta charset="utf-8">
<title>Top Talents For Your Company</title>
<link href="https://fonts.googleapis.com/css2?family=Lato:wght@400;700&display=swap" rel="stylesheet">
<style>
:root{
  --ink:#2a2a2a;
  --text:#333333;
  --muted:#8a8a8a;
  --card:#eeeeee;
  --accent:#f5474b;
  --link:#3d8fd6;
  --rule:#c8c8c8;
  --paper:#ffffff;
  --avatar-a:#6b4a3e;
  --avatar-b:#2b2b2b;
}
*{margin:0;padding:0;box-sizing:border-box}
html,body{width:863px;height:1200px;overflow:hidden;background:var(--paper)}
body{position:relative;font-family:'Lato',sans-serif;color:var(--text)}
.brand{position:absolute;left:107px;top:36px;display:flex;align-items:center;gap:10px}
.brand-mark{width:30px;height:30px;background:var(--ink);border-radius:50%}
.brand-name{font-size:17px;font-weight:700;color:var(--ink);letter-spacing:.5px}
.headline{position:absolute;left:103px;top:128px;font-size:41px;font-weight:700;line-height:47px;letter-spacing:2px;color:var(--ink)}
.greeting{position:absolute;left:110px;top:264px;font-size:13px;line-height:17px;color:var(--text)}
.candidate{position:absolute;left:95px;width:661px;height:349px;background:var(--card)}
.candidate--first{top:345px}
.candidate--second{top:715px}
.avatar{position:absolute;left:57px;top:14px;width:75px;height:75px;border-radius:50%;border:3px solid var(--paper);background:linear-gradient(160deg,var(--avatar-a),var(--avatar-b))}
.c-name{position:absolute;left:156px;top:30px;font-size:17px;color:var(--ink)}
.c-role{position:absolute;left:156px;top:55px;font-size:15px;color:var(--muted)}
.label{position:absolute;right:528px;font-size:12.5px;color:var(--muted);text-align:right;line-height:16px}
.value{position:absolute;left:156px;font-size:12.5px;color:var(--text);line-height:17px;white-space:nowrap}
.value .date{margin-left:6px}
.btn{position:absolute;left:153px;top:292px;width:102px;height:25px;border-radius:6px;background:var(--accent);color:var(--paper);font-size:12.5px;line-height:25px;text-align:center;text-decoration:none}
.help{position:absolute;left:105px;top:1078px;font-size:12.5px;line-height:17px;color:var(--text)}
.help a{color:var(--link);text-decoration:none}
.rule{position:absolute;left:100px;top:1126px;width:656px;height:2px;background:var(--rule)}
.footer{position:absolute;left:101px;top:1163px;font-size:12.5px;color:var(--text)}
</style>
</head>
<body>
<div class="brand"><span class="brand-mark"></span><span class="brand-name">Northbridge Talent</span></div>

<h1 class="headline">Top Talents<br>For Your Company</h1>

<p class="greeting">Hi,<br>We have got some of the top talents for<br>&lt;The Position Name&gt;</p>

<section class="candidate candidate--first">
  <div class="avatar" role="img" aria-label="Candidate portrait photo"></div>
  <div class="c-name">Marco Ellison</div>
  <div class="c-role">Software Engineer</div>
  <div class="label" style="top:102px">Experince:</div>
  <div class="value" style="top:102px">7 years</div>
  <div class="label" style="top:124px">Work:</div>
  <div class="value" style="top:124px">Software Engineer . Quillora<span class="date">Jan ‘15 - Feb ‘18</span></div>
  <div class="value" style="top:146px">Software Engineer . Brenfield Consulting<span class="date">&nbsp;&nbsp;Oct ‘14 - Jan ‘15</span></div>
  <div class="label" style="top:180px">School:</div>
  <div class="value" style="top:180px">University of Westmere2013<br>BA German Studies</div>
  <div class="value" style="top:225px">University of Westmere2013<br>BSE Computer Science and Engineering</div>
  <a class="btn" href="#">View Profile</a>
</section>

<section class="candidate candidate--second">
  <div class="avatar" role="img" aria-label="Candidate portrait photo"></div>
  <div class="c-name">Marco Ellison</div>
  <div class="c-role">Software Engineer</div>
  <div class="label" style="top:102px">Experince:</div>
  <div class="value" style="top:102px">7 years</div>
  <div class="label" style="top:124px">Work:</div>
  <div class="value" style="top:124px">Software Engineer . Quillora<span class="date">&nbsp;&nbsp;Jan ‘15 - Feb ‘18</span></div>
  <div class="value" style="top:146px">Software Engineer . Brenfield Consulting<span class="date">&nbsp;&nbsp;&nbsp;Oct ‘14 - Jan ‘15</span></div>
  <div class="label" style="top:180px">School:</div>
  <div class="value" style="top:180px">University of Westmere2013<br>BA German Studies</div>
  <div class="value" style="top:225px">University of Westmere2013<br>BSE Computer Science and Engineering</div>
  <a class="btn" href="#">View Profile</a>
</section>

<p class="help">Need help?<br>Contact <a href="#">Customer Support</a> for assistance</p>
<div class="rule"></div>
<p class="footer">© 2019 - The Northbridge Industry Network.</p>
</body>
</html>
```